Non-Profit org for new mothers in distress in need of website design

We need a website for our non-profit organization, Cradlewell Alliance of Florida, based in Sarasota, Florida. We provide peer support for new moms in distress, trainings for mental health professionals, education and resources for our providers, and an intensive volunteer training program. We need a site that is calming yet energizing, simple, yet informative, with minimal pages and text. Our goal is to be a point of contact for mothers to find local resources whatever their need, so our most important feature we need is at least 4 zip code look-ups for users to find 1. Local volunteers, 2. Support Groups, 3. Trained Mental Health Professionals, 4. Other Health and Wellness Support Providers. Ideally I would like the zip code lookups on the home page sort of interest-layout-style, with the following pages: About Us, PPD Facts, For Parents, For Providers, Donate, Contact, and Blog. Because we are a very small non-profit - under 20 volunteers, no paid staff, donation funded, under $10,000 budget all going to service programs, we can't afford much, but are willing to pay a reasonable fee for quality work. Currently we have an active site through plonto... www.cradlewellhaven.org. The site either needs to be polished or overhauled. And we need a more professional zip code L/U. Thank you so much for your time and interest - we look forward to working with you.
Best,
Maren Tolliver

Reason: Hoping for a couple more changes and clearance with decision-making committee.

Target Market(s)

New mothers with babies and young children, new fathers and perinatal providers

Industry/Entity Type

Non Profit

Number of Pages Required

5+ page

Font styles to use
Sans Serif

Colors
886aae

Requirements
Must have
• contact form, zip code lookup, video embedded, calm and energizing tone
Nice to have
• boardly-style layout
Should not have
• complicated navigation, heavy text,

```html
<!DOCTYPE html>
<html lang="en">
<head>
<meta charset="utf-8">
<title>Cradlewell Alliance of Florida</title>
<link href="https://fonts.googleapis.com/css2?family=Roboto:wght@300;400;500&display=swap" rel="stylesheet">
<style>
:root{
  --purple:#8b6aae;
  --purple-dark:#5e4480;
  --purple-nav-active:#6f5293;
  --ink:#333;
  --text:#555;
  --muted:#777;
  --line:#d8d8d8;
  --grey-band:#f0f0f0;
  --grey-light:#f7f7f7;
  --btn-grey:#9a9a9a;
  --white:#fff;
}
*{box-sizing:border-box;margin:0;padding:0}
html,body{width:1200px;height:2239px;overflow:hidden}
body{position:relative;font-family:"Roboto",Arial,sans-serif;color:var(--text);background:var(--white)}
.abs{position:absolute}

/* hero */
.hero{left:0;top:0;width:1200px;height:480px;background:linear-gradient(90deg,#f3f3f1 0%,#efefed 45%,#e9e6e2 100%)}
.hero-photo{left:492px;top:0;width:708px;height:480px;background:linear-gradient(110deg,#ece9e5 0%,#e2d4c8 35%,#d8bfae 55%,#f1eeec 80%,#f7f7f7 100%)}
.logo-box{left:133px;top:16px;width:108px;height:116px;background:var(--white);border:1px solid #e2e2e2;border-radius:3px;box-shadow:0 1px 3px rgba(0,0,0,.08);display:flex;align-items:center;justify-content:center;text-align:center;gap:6px;flex-direction:column}
.logo-box .dot{width:14px;height:14px;border-radius:50%;background:var(--purple)}
.logo-box span{font-size:12px;line-height:1.3;color:var(--purple);font-weight:500}
.mission-title{left:133px;top:168px;font-size:31px;font-weight:300;color:var(--ink)}
.mission-text{left:133px;top:213px;width:300px;font-size:14px;line-height:19px;color:var(--text)}
.field{background:var(--white);border:1px solid #d6d6d6;border-radius:2px;height:36px;font-size:11px;color:#666;padding:0 13px;display:flex;align-items:center}
.btn-contact{left:133px;top:409px;width:96px;height:33px;background:linear-gradient(#6d6d6d,#555);color:var(--white);font-size:10.5px;display:flex;align-items:center;justify-content:center;border-radius:2px;letter-spacing:.2px}
.slider-dots{left:557px;top:444px;display:flex;gap:16px}
.slider-dots i{width:7px;height:7px;border-radius:50%;background:#cfcfcf}
.slider-dots i:first-child{background:#777}

/* nav */
.nav{left:0;top:480px;width:1200px;height:40px;background:var(--purple)}
.nav ul{list-style:none;position:absolute;left:133px;top:0;display:flex;height:40px;border-left:1px solid rgba(255,255,255,.25)}
.nav li{height:40px;display:flex;align-items:center;justify-content:center;color:var(--white);font-size:11.5px;border-right:1px solid rgba(255,255,255,.25)}
.nav li.active{background:var(--purple-nav-active)}

/* intro */
.intro-head{left:0;top:562px;width:1200px;text-align:center;font-size:27px;font-weight:300;color:#222}
.intro-text{left:133px;top:608px;width:934px;text-align:center;font-size:11.5px;line-height:20px;color:var(--text)}
.section-label{width:1200px;left:0;text-align:center;font-size:20px;color:var(--purple);font-weight:400}
.zip{width:318px;height:41px;border:1px solid #cfcfcf;background:var(--white);display:flex}
.zip span{flex:1;font-size:11px;color:#777;padding-left:17px;display:flex;align-items:center}
.zip b{width:33px;background:var(--btn-grey);display:flex;align-items:center;justify-content:center}

/* goals */
.goals{left:0;top:826px;width:1200px;height:541px;background:var(--grey-band)}
.goals-title{left:0;top:866px;width:1200px;text-align:center;font-size:26px;font-weight:300;color:#555}
.goal-col{width:300px}
.goal-col h3{font-size:19px;font-weight:500;color:var(--purple);margin:14px 0 12px}
.goal-col ul{list-style:none}
.goal-col li{position:relative;padding-left:13px;font-size:10.5px;line-height:15px;color:#666;margin-bottom:9px}
.goal-col li::before{content:"";position:absolute;left:2px;top:6px;width:3px;height:3px;border-radius:50%;background:#888}
.funding{left:133px;top:1225px;width:607px;height:102px;background:var(--white);border:1px solid #ddd}
.funding h4{position:absolute;left:28px;top:17px;font-size:18px;font-weight:500;color:#666;line-height:24px}
.funding ul{position:absolute;left:172px;top:16px;list-style:none}
.funding li{position:relative;padding-left:13px;font-size:10.5px;line-height:15px;color:#666;margin-bottom:7px}
.funding li::before{content:"";position:absolute;left:2px;top:6px;width:3px;height:3px;border-radius:50%;background:#888}

.providers-band{left:0;top:1367px;width:1200px;height:126px;background:var(--grey-light)}

/* video + accordion */
.video-title{left:133px;top:1541px;font-size:19px;font-weight:300;color:#333}
.video{left:133px;top:1575px;width:442px;height:283px;background:linear-gradient(135deg,#f2f1ef 0%,#e8e4df 40%,#d9cfc6 65%,#eceae7 100%)}
.play{left:338px;top:1701px;width:32px;height:32px;border-radius:50%;background:var(--purple-dark);display:flex;align-items:center;justify-content:center}
.acc{left:622px;width:444px;height:39px;border:1px solid #dcdcdc;background:var(--white);display:flex;align-items:center;padding-left:12px;font-size:14px;color:#555;gap:10px}
.acc i{width:14px;height:14px;border:1px solid #999;position:relative;display:block}
.acc i::before{content:"";position:absolute;left:2px;right:2px;top:6px;height:1px;background:#777}
.acc i.plus::after{content:"";position:absolute;top:2px;bottom:2px;left:6px;width:1px;background:#777}
.risk-list{left:640px;top:1600px;list-style:none;width:420px}
.risk-list li{position:relative;padding-left:10px;font-size:10px;line-height:13.5px;color:#555;margin-bottom:5.8px}
.risk-list li::before{content:"";position:absolute;left:0;top:5px;width:3px;height:3px;border-radius:50%;background:#777}

/* lookups */
.lookups{left:0;top:1925px;width:1200px;height:136px;background:var(--grey-band)}
.lookup-label{font-size:16px;color:var(--purple)}
.lookup .zip{width:254px;height:40px}

/* contact row */
.contact-item{top:2098px;font-size:12px;color:#444;display:flex;align-items:center;gap:9px}
.socials{left:975px;top:2093px;display:flex;gap:7px}
.socials i{width:25px;height:25px;border-radius:50%;background:#c9c9c9}
.socials i:first-child{background:#3f5b9c}

/* footer */
.footer{left:0;top:2143px;width:1200px;height:96px;background:var(--purple-dark)}
.footer-links{left:133px;top:2169px;font-size:10.5px;color:#e8e0f2}
.footer-links span{margin:0 6px;color:#b7a5cc}
.copyright{left:133px;top:2196px;font-size:10.5px;color:#e8e0f2}
.to-top{left:1028px;top:2171px;width:38px;height:38px;border-radius:50%;border:2px solid #8f78ad;display:flex;align-items:center;justify-content:center}
</style>
</head>
<body>

<!-- hero -->
<section class="abs hero" aria-label="Hero"></section>
<div class="abs hero-photo" role="img" aria-label="Photo of a smiling mother lifting her baby above her"></div>
<div class="abs logo-box"><i class="dot"></i><span>Cradlewell<br>Alliance</span></div>
<h1 class="abs mission-title">Our Mission</h1>
<p class="abs mission-text">Our mission is to ease the transition from pregnancy to parenthood</p>
<div class="abs field" style="left:133px;top:266px;width:164px">Name</div>
<div class="abs field" style="left:307px;top:266px;width:166px">Email</div>
<div class="abs field" style="left:133px;top:312px;width:164px">Phone</div>
<div class="abs field" style="left:307px;top:312px;width:166px">City</div>
<div class="abs field" style="left:133px;top:361px;width:340px">Message</div>
<div class="abs btn-contact">CONTACT US</div>
<div class="abs slider-dots"><i></i><i></i><i></i><i></i></div>

<!-- navigation -->
<nav class="abs nav">
  <ul>
    <li class="active" style="width:100px">HOME</li>
    <li style="width:124px">ABOUT US</li>
    <li style="width:90px">PPD</li>
    <li style="width:131px">FOR MOMS</li>
    <li style="width:157px">FOR PROVIDERS</li>
    <li style="width:114px">DONATE</li>
    <li style="width:118px">CONTACT</li>
    <li style="width:98px">BLOG</li>
  </ul>
</nav>

<!-- intro -->
<h2 class="abs intro-head">You are not alone.You are not to blame. With help and effort, you will be well.</h2>
<p class="abs intro-text">Find your Cradlewell KINDREDMom Volunteer today with the locator below. Your area KINDREDMom will listen, connect you with Support Groups, counselors, therapists &amp; psychiatrists with training in PPD near you, doulas, wellness and more to encourage your PPD recovery. Your KINDREDMom is a trained volunteer and PPD overcomer - call or email her today.</p>
<h3 class="abs section-label" style="top:694px">Trained Mental Health Professionals</h3>
<div class="abs zip" style="left:442px;top:725px"><span>Enter your Zipcode</span><b><svg width="10" height="16" viewBox="0 0 10 16"><path d="M2 2l6 6-6 6" fill="none" stroke="#fff" stroke-width="2"/></svg></b></div>

<!-- goals -->
<section class="abs goals" aria-label="Goals"></section>
<h2 class="abs goals-title">What is CAF actively doing to achieve these goals?</h2>

<div class="abs goal-col" style="left:133px;top:936px">
  <svg width="28" height="28" viewBox="0 0 28 28"><path d="M7 4h15v18H9a3 3 0 0 0-3 3V7a3 3 0 0 1 1-3z" fill="var(--purple)"/><path d="M9 22h13v3H9a1.5 1.5 0 0 1 0-3z" fill="none" stroke="var(--purple)" stroke-width="1.5"/><path d="M10 9h9M10 13h9" stroke="#fff" stroke-width="1.5"/></svg>
  <h3>Education</h3>
  <ul>
    <li>Planning "Providers and Postpartum Adjustment" Q&amp;A at libraries</li>
    <li>Compiling a provider resource list</li>
    <li>Offering all providers opportunity for Postpartum Adjustment In-Service</li>
    <li>Joining local Perinatal Service Networks and Coalitions</li>
    <li>Speaking at Childbirth Education classes about Postpartum Adjustment</li>
  </ul>
</div>

<div class="abs goal-col" style="left:461px;top:936px">
  <svg width="34" height="30" viewBox="0 0 34 30"><circle cx="11" cy="17" r="7" fill="none" stroke="var(--purple)" stroke-width="4" stroke-dasharray="3 2.5"/><circle cx="11" cy="17" r="3" fill="var(--purple)"/><circle cx="25" cy="8" r="5" fill="none" stroke="var(--purple)" stroke-width="3" stroke-dasharray="2.5 2"/><circle cx="26" cy="23" r="4" fill="none" stroke="var(--purple)" stroke-width="3" stroke-dasharray="2 2"/></svg>
  <h3>Preparation</h3>
  <ul>
    <li>Conducting Personality and Postpartum Adjustment Project to examine potential relationship between personality and risk factors for PMAD</li>
    <li>Collaborating with local Childbirth and Parenting Educators to create free "Postpartum Prep" Class for expectant and pre-expectant parents</li>
  </ul>
</div>

<div class="abs goal-col" style="left:790px;top:936px">
  <svg width="30" height="30" viewBox="0 0 30 30"><circle cx="15" cy="15" r="12" fill="none" stroke="var(--purple)" stroke-width="4"/><circle cx="15" cy="15" r="5" fill="none" stroke="var(--purple)" stroke-width="2.5"/><path d="M6.5 6.5l5 5M23.5 6.5l-5 5M6.5 23.5l5-5M23.5 23.5l-5-5" stroke="var(--purple)" stroke-width="3"/></svg>
  <h3>Support</h3>
  <ul>
    <li>Conducting peer support volunteer training Dec thru Jan</li>
    <li>Developing materials to be distributed to new mothers at local hospitals</li>
    <li>Creating KINDRED, a pre-arranged telephone peer support program where a volunteer/ momcontacts mom at "touchpoint" times in her recovery</li>
    <li>Establishing biweekly Postpartum Adjustment Support Groups at BVMC</li>
    <li>Giving "Mom and Baby Talks" at local moms groups to break the silence</li>
    <li>Collaborating with area Pediatricians to distribute PPD Flyer at 2 mo appt.</li>
    <li>Collaborating with area Obstetricians to distribute PPD Flyer at 6 wk appt.</li>
  </ul>
</div>

<div class="abs funding">
  <h4>Funding and<br>More</h4>
  <ul>
    <li>Pursuing 501(c)(3) status (application pending)</li>
    <li>Researching and preparing grant applications and fundraising ideas</li>
    <li>Seeking volunteers</li>
  </ul>
</div>

<!-- other providers -->
<section class="abs providers-band" aria-label="Other providers lookup"></section>
<h3 class="abs section-label" style="top:1392px">Other Health and Wellness Support Providers</h3>
<div class="abs zip" style="left:442px;top:1424px"><span>Enter your Zipcode</span><b><svg width="10" height="16" viewBox="0 0 10 16"><path d="M2 2l6 6-6 6" fill="none" stroke="#fff" stroke-width="2"/></svg></b></div>

<!-- video + accordion -->
<h3 class="abs video-title">Featured Video</h3>
<div class="abs video" role="img" aria-label="Video still of a baby lying on a white blanket"></div>
<div class="abs play"><svg width="12" height="14" viewBox="0 0 12 14"><path d="M2 1l9 6-9 6z" fill="#fff"/></svg></div>

<div class="abs acc" style="top:1548px"><i></i>The Risk Factors</div>
<ul class="abs risk-list">
  <li>Family OR personal history of mood illness<br>(i.e. addiction, depression, panic attacks, anxiety)</li>
  <li>Stressful life events around the time of birth</li>
  <li>Poor system of support</li>
  <li>Relationship/Marital problems</li>
  <li>Women with severe PMS symptoms</li>
  <li>Mood changes while taking birth control or fertility drugs</li>
  <li>A prior episode of PPD, depressive and/or anxiety symptoms during pregnancy</li>
</ul>
<div class="abs acc" style="top:1763px"><i class="plus"></i>The Warning Signs (after 3rd week postpartum)</div>
<div class="abs acc" style="top:1819px"><i class="plus"></i>What to do when you recognize some of the warning signs :</div>

<!-- lookups -->
<section class="abs lookups" aria-label="Zip code lookups"></section>
<div class="abs lookup" style="left:133px;top:1956px">
  <div class="lookup-label">Local volunteers</div>
  <div class="zip" style="margin-top:9px"><span>Enter your Zipcode</span><b><svg width="10" height="16" viewBox="0 0 10 16"><path d="M2 2l6 6-6 6" fill="none" stroke="#fff" stroke-width="2"/></svg></b></div>
</div>
<div class="abs lookup" style="left:472px;top:1956px">
  <div class="lookup-label">Support Groups</div>
  <div class="zip" style="margin-top:9px"><span>Enter your Zipcode</span><b><svg width="10" height="16" viewBox="0 0 10 16"><path d="M2 2l6 6-6 6" fill="none" stroke="#fff" stroke-width="2"/></svg></b></div>
</div>
<div class="abs lookup" style="left:812px;top:1956px">
  <div class="lookup-label">Zip code search</div>
  <div class="zip" style="margin-top:9px"><span>Search</span><b><svg width="10" height="16" viewBox="0 0 10 16"><path d="M2 2l6 6-6 6" fill="none" stroke="#fff" stroke-width="2"/></svg></b></div>
</div>

<!-- contact row -->
<div class="abs contact-item" style="left:133px"><svg width="9" height="13" viewBox="0 0 9 13"><path d="M4.5 0A4.5 4.5 0 0 0 0 4.5C0 8 4.5 13 4.5 13S9 8 9 4.5A4.5 4.5 0 0 0 4.5 0zm0 6.3a1.8 1.8 0 1 1 0-3.6 1.8 1.8 0 0 1 0 3.6z" fill="#444"/></svg>4127 Palmetto Grove Ave., Sarasota, FL</div>
<div class="abs contact-item" style="left:483px"><svg width="12" height="12" viewBox="0 0 12 12"><path d="M2.5 0l2 3-1.3 1.4a7 7 0 0 0 4.4 4.4L9 7.5l3 2-1.2 2.3C5 12 0 7 .2 1.2z" fill="#444"/></svg>Call us on : 941.555.0148</div>
<div class="abs contact-item" style="left:706px"><svg width="13" height="10" viewBox="0 0 13 10"><rect width="13" height="10" fill="#444"/><path d="M0 0l6.5 5.5L13 0" fill="none" stroke="#fff" stroke-width="1.2"/></svg>Email : maren@cradlewellhaven.org</div>
<div class="abs socials"><i></i><i></i><i></i></div>

<!-- footer -->
<footer class="abs footer"></footer>
<div class="abs footer-links">Home<span>|</span>About Us<span>|</span>PPD<span>|</span>For Moms<span>|</span>For Providers<span>|</span>Donate<span>|</span>Contact<span>|</span>Blog</div>
<div class="abs copyright">Copyright &copy; 2016 &nbsp;Cradlewell KINDREDMom Volunteer. &nbsp;All rights reserved.</div>
<div class="abs to-top"><svg width="16" height="18" viewBox="0 0 16 18"><path d="M8 16V3M2 8l6-6 6 6" fill="none" stroke="#8f78ad" stroke-width="2.2"/></svg></div>

</body>
</html>
```